Pipelining Product Supply Company Needs New Stationery

We need new stationery (letter head, with compliments slips & business card) for our industry leading pipe lining supply company. basically we sell product to other plumbers to carry out pipe relining.

Im looking for something, fresh, professional, sleek and modern at the same time.

Ive attached a copy of the logo and also some guidelines to follow for colours and fonts etc.

Target Market(s)

Plumbers

Industry/Entity Type

Plumbing

Font styles to use
Sans Serif

Requirements
Must have
• The logo, space for ABN, Address, Phone Number, website and email.
Nice to have
• Stand out from the crowd. To look sleep and professional.
Should not have
• Any other colours apart from what is on the guidelines.

```html
<!DOCTYPE html>
<html lang="en">
<head>
<meta charset="utf-8">
<title>Harbourline Relining Supplies – Stationery</title>
<link href="https://fonts.googleapis.com/css2?family=Roboto:wght@400;500;700&family=Roboto+Condensed:ital,wght@1,700&display=swap" rel="stylesheet">
<style>
  :root{
    --bg:#eeeeee;
    --paper:#ffffff;
    --green:#8dc63f;
    --grey:#98989b;
    --ink:#2f2f2f;
    --muted:#8a8a8a;
    --night:#050a10;
  }
  *{box-sizing:border-box;margin:0;padding:0}
  html,body{width:1200px;height:941px;overflow:hidden;background:var(--bg);font-family:"Roboto",Arial,sans-serif;color:var(--ink)}
  .sheet{position:absolute;background:var(--paper);box-shadow:0 8px 14px rgba(0,0,0,.16)}
  .brand{color:var(--green);font-weight:500;line-height:1.1;letter-spacing:.2px;white-space:nowrap}
  .brand span{display:block}
  .band{position:absolute;left:0;right:0;bottom:0}
  .band svg{display:block;width:100%;height:100%}
  .abn{color:var(--green)}
  .small{font-size:7.2px;line-height:1.35;color:var(--ink)}
  .small *{color:inherit}
  .small .abn{color:var(--green)}

  /* letterhead */
  .letterhead{left:75px;top:141px;width:512px;height:683px}
  .letterhead .brand{position:absolute;left:42px;top:48px;font-size:17px}
  .letterhead .footer{position:absolute;left:41px;top:618px;display:flex;gap:10px}
  .letterhead .divider{width:1px;background:#666;height:29px}
  .contacts div{display:flex;align-items:center;gap:4px}
  .letterhead .band{height:18px}

  /* business cards */
  .card-front{left:626px;top:138px;width:233px;height:135px}
  .card-front .brand{position:absolute;left:22px;top:50px;font-size:10px}
  .card-front .rule{position:absolute;left:117px;top:32px;width:1px;height:66px;background:#999}
  .card-front .details{position:absolute;left:129px;top:31px;font-size:5.2px;line-height:1.3;color:var(--ink)}
  .card-front .name{color:var(--green);font-size:8.5px;font-weight:500}
  .card-front .role{font-size:5px;margin-bottom:6px}
  .card-front .details div{display:flex;align-items:center;gap:3px}
  .card-front .band{height:9px}
  .card-back{left:878px;top:138px;width:234px;height:135px;background:var(--night)}
  .card-back .brand{position:absolute;left:0;right:0;top:48px;text-align:center;font-size:16px}

  /* envelope */
  .envelope{left:626px;top:318px;width:513px;height:234px}
  .envelope svg{position:absolute;left:0;top:0}

  /* compliments slip */
  .slip{left:627px;top:592px;width:510px;height:232px}
  .slip .brand{position:absolute;left:22px;top:30px;font-size:14px}
  .slip .address{position:absolute;left:22px;top:82px}
  .slip .title{position:absolute;right:29px;top:36px;font-family:"Roboto Condensed",Arial,sans-serif;font-style:italic;font-weight:700;font-size:20px;color:var(--muted)}
  .slip .band{height:16px}
</style>
</head>
<body>

<section class="sheet letterhead">
  <div class="brand"><span>Harbourline</span><span>Relining Supplies</span></div>
  <div class="footer small">
    <div><span class="abn">ABN</span> 00000008<br>55 demo street, demo place<br>P.O. Box 000, 555 Avenue</div>
    <div class="divider"></div>
    <div class="contacts">
      <div><svg width="7" height="7" viewBox="0 0 10 10"><path d="M2 1l2 2-1 1.5a6 6 0 0 0 2.5 2.5L7 6l2 2-1.5 1.5C4 9 1 6 .5 2.5z" fill="var(--green)"/></svg><span>888-8888-8888</span></div>
      <div><svg width="7" height="7" viewBox="0 0 10 10"><rect x="0" y="2" width="10" height="6" fill="var(--green)"/><path d="M0 2l5 3 5-3" stroke="#fff" fill="none"/></svg><span>info@websitename.com</span></div>
      <div><svg width="7" height="7" viewBox="0 0 10 10"><circle cx="5" cy="5" r="4.3" stroke="var(--green)" fill="none"/><path d="M1 5h8M5 1v8" stroke="var(--green)"/></svg><span>www.websitename.com</span></div>
    </div>
  </div>
  <div class="band"><svg viewBox="0 0 512 18" preserveAspectRatio="none"><rect width="512" height="18" fill="var(--grey)"/><polygon points="0,0 269,0 251,18 0,18" fill="var(--green)"/></svg></div>
</section>

<section class="sheet card-front">
  <div class="brand"><span>Harbourline</span><span>Relining Supplies</span></div>
  <div class="rule"></div>
  <div class="details">
    <div class="name">Daniel Crane</div>
    <div class="role">Founder</div>
    <p><span class="abn">ABN</span> 00000008<br>55 demo street, demo place<br>P.O. Box 000, 555 Avenue</p>
    <p style="margin-top:4px"></p>
    <div><svg width="5" height="5" viewBox="0 0 10 10"><path d="M2 1l2 2-1 1.5a6 6 0 0 0 2.5 2.5L7 6l2 2-1.5 1.5C4 9 1 6 .5 2.5z" fill="var(--green)"/></svg><span>888-8888-8888</span></div>
    <div><svg width="5" height="5" viewBox="0 0 10 10"><rect y="2" width="10" height="6" fill="var(--green)"/></svg><span>info@websitename.com</span></div>
    <div><svg width="5" height="5" viewBox="0 0 10 10"><circle cx="5" cy="5" r="4" fill="var(--green)"/></svg><span>www.websitename.com</span></div>
  </div>
  <div class="band"><svg viewBox="0 0 233 9" preserveAspectRatio="none"><rect width="233" height="9" fill="var(--grey)"/><polygon points="0,0 120,0 114,9 0,9" fill="var(--green)"/></svg></div>
</section>

<section class="sheet card-back">
  <div class="brand"><span>Harbourline</span><span>Relining Supplies</span></div>
</section>

<section class="sheet envelope">
  <svg width="513" height="234" viewBox="0 0 513 234">
    <path d="M1 0 Q4 56 18 66 Q24 70 40 70 H473 Q489 70 495 66 Q509 56 512 0" fill="#fff" stroke="#e6e8dc" stroke-width="1.2"/>
  </svg>
</section>

<section class="sheet slip">
  <div class="brand"><span>Harbourline</span><span>Relining Supplies</span></div>
  <div class="address small"><span class="abn">ABN</span> 00000008<br>55 demo street, demo place<br>P.O. Box 000, 555 Avenue</div>
  <div class="title">With Compliment</div>
  <div class="band"><svg viewBox="0 0 510 16" preserveAspectRatio="none"><rect width="510" height="16" fill="var(--grey)"/><polygon points="0,0 261,0 245,16 0,16" fill="var(--green)"/></svg></div>
</section>

</body>
</html>
```